QVT Web Design Project

I would like a simple and elegant design for my international business consulting practice web site. I already have new QVT Logo and will have brochure-colors are blue, green and black

Practice areas:
I offer consulting services specializing in developing Internet-based anti-counterfeiting and anti-fraud programs, test purchases and investigations.

I offer Cyber Security, Data Protection and Compliance services

I also offer International Due Diligence Investigations and Country and Travel Risk Assessments

General Background Investigations

Physical Security Services

About me section listing my Bio

I have a set of key associates that I work with around the world and will want to list their CVs or Bios under "QVT

Associates"Banner with nice photo but not too cluttered

Ability to Upload documents and articles

Contact us section
Updates

I have uploaded my new logo-please advise if you didn't get it or it is not in the correct file format.

Thank you

Gordon

Hello Everyone,

Thank you for your submissions and ideas. I'm not sure about design only vs code. I understand that some of you do not do code-if not then please just provide design.

More about my business: see below link on Sharebox files to my brochure-this should help but don't use that phone number-see below.

https://files.sharebox.example/viewer?a=v&pid=explorer&srcid=0Q-4PX9nRfwqeMkTuZ3B8NHhsLWVmXy00ZWQ3LTkyOGQtZmQ1ZTg0YjE2OXB4&hl=en_US

 

Here are some details.

Contacts:

Gordon T. Falkirk, CPP

President

Falkirk and Associates, LLC

P.O. Box 41927

Gaithersburg, MD 20871

USA

web address:www.Falkirkandassociates.example (currently not working)

email:gord @falkirkand associates.example

Tel: 202-555-0147

I hope this is helpful. Gord

Reason: Sorry but during holiday period, have not had as much time to devote to this project. Thanks for your submissions.

Per my previous guidance, please keep designs simple and elegant and free from traditional security images with locks and chains-I prefer one or at most, two photos. Two colors- blue and green in addition to black for print. I want to present professional, corporate and international image. Thank you for your ideas nad submissions.

Gord

Target Market(s)

Law firms, large multi-national corporations, Security Industry

Industry/Entity Type

Business

Requirements
Must have
• Must have sections: (will provide text)

About QVT (will provide text)

Practice areas

Associates (will provide text)

Contact us

(it must also have ability to upload files and articles)
Should not have
• Old style fonts and symbols such as security badges, scales of justice, etc. I want a sleek and modern design.

```html
<!DOCTYPE html>
<html lang="en">
<head>
<meta charset="utf-8">
<title>QVT | Falkirk &amp; Associates, LLC</title>
<link href="https://fonts.googleapis.com/css2?family=Questrial&family=Ubuntu:wght@400&display=swap" rel="stylesheet">
<style>
:root{
  --page:#000;
  --navy:#0b3f70;
  --navy-deep:#062d55;
  --blue:#0c4e8c;
  --sky:#3d9bd8;
  --logo:#1c4f86;
  --text:#c8d7e8;
  --muted:#8fa9c4;
  --green:#8bd13f;
  --white:#fff;
  --line:#1f5d96;
}
*{box-sizing:border-box;margin:0;padding:0}
html,body{width:1200px;height:1004px;overflow:hidden;background:var(--page)}
body{position:relative;font-family:Arial,Helvetica,sans-serif;color:var(--text)}
.abs{position:absolute}
.site-header{left:24px;top:30px;width:1150px;height:74px;background:linear-gradient(#ffffff,#dcdcdc)}
.brand{left:18px;top:6px;font-family:"Ubuntu",sans-serif;color:var(--logo);font-size:25px;white-space:nowrap}
.brand .sep{display:inline-block;width:1px;height:30px;background:var(--logo);vertical-align:middle;margin:0 8px}
.tagline{left:20px;top:44px;font-family:"Ubuntu",sans-serif;font-size:15px;letter-spacing:1.6px;color:var(--logo)}
.callus{right:20px;top:10px;font-size:15px;color:#555;white-space:nowrap}
.callus b{font-weight:normal;font-size:30px;color:var(--logo);vertical-align:-3px}
.banner{left:24px;top:104px;width:1150px;height:256px;background:linear-gradient(180deg,#0a4c85,#083d6e)}
.headline{left:86px;top:140px;width:560px;font-family:"Questrial",sans-serif;font-size:35px;line-height:43px;color:var(--white)}
.hero-art{left:666px;top:80px;width:400px;height:268px;border-radius:6px;background:radial-gradient(ellipse at 45% 40%,#9ec6e6,#3e6e99 55%,rgba(8,61,110,0) 75%)}
.slide-arrow{top:217px;width:26px;height:36px;background:#1e3c5c}
.slide-arrow svg{display:block;margin:12px auto}
.nav{left:24px;top:360px;width:1150px;height:40px;background:linear-gradient(#11558f,#0c487c);border-top:1px solid #2c6ba3;border-bottom:1px solid #05335e}
.nav a{position:absolute;top:12px;font-size:14px;color:#0a2d50;text-decoration:none;transform:translateX(-50%)}
.nav a.active{color:#4b87bd;font-weight:bold}
.nav .div{position:absolute;top:0;width:1px;height:40px;background:#0a3a66}
.nav .pointer{position:absolute;left:79px;top:39px;width:0;height:0;border-left:12px solid transparent;border-right:12px solid transparent;border-top:10px solid #0c487c}
.search{left:955px;top:368px;width:197px;height:26px;background:#1a5b95;border:1px solid #0a3a66}
.main{left:24px;top:400px;width:1150px;height:550px;background:linear-gradient(180deg,#0a3e6f,#0b4a86)}
.vdiv{left:658px;top:422px;width:1px;height:470px;background:var(--line)}
.hdiv{left:34px;top:694px;width:624px;height:1px;background:var(--line)}
h2{position:absolute;font-family:"Questrial",sans-serif;font-weight:normal;font-size:22px;color:var(--white)}
h2.accent{color:var(--sky)}
p.copy{position:absolute;font-size:13.4px;line-height:17.4px;color:var(--text)}
.more{position:absolute;font-size:13.4px;color:var(--green)}
.more span{color:#4ea34a}
.ph{position:absolute}
.addr{left:674px;top:775px;width:242px;height:150px;background:#0a3560;padding:14px 22px;font-size:13.4px;line-height:17.4px;color:var(--muted)}
.footer{left:28px;top:972px;font-size:11px;color:#1b4f85}
.footer a{color:#2e6fb4;text-decoration:none}
.social{left:1000px;top:960px;width:166px;height:34px;background:#111;border-radius:3px}
.social i{position:absolute;top:5px;width:24px;height:24px;border-radius:50%}
</style>
</head>
<body>
<header class="abs site-header">
  <div class="abs brand">QVT<span class="sep"></span>Falkirk &amp; Associates, LLC</div>
  <div class="abs tagline">Intellectual Property and Cyber Security</div>
  <div class="abs callus">Call us - <b>543 555 0188</b></div>
</header>

<section class="abs banner"></section>
<div class="abs hero-art" role="img" aria-label="Illustration of a monitor showing a fingerprint with a padlock and a security camera"></div>
<h1 class="abs headline" style="font-weight:normal">Security of your buisness data, network, and the physical premises is important for the future of the business.</h1>
<div class="abs slide-arrow" style="left:24px"><svg width="8" height="12"><path d="M7 0L0 6l7 6z" fill="#6e8aa6"/></svg></div>
<div class="abs slide-arrow" style="left:1148px"><svg width="8" height="12"><path d="M1 0l7 6-7 6z" fill="#6e8aa6"/></svg></div>

<nav class="abs nav">
  <a class="active" style="left:80px">Home</a>
  <span class="div" style="left:157px"></span>
  <a style="left:250px">About QVT</a>
  <span class="div" style="left:338px"></span>
  <a style="left:434px">Practice Areas</a>
  <span class="div" style="left:532px"></span>
  <a style="left:628px">Associates</a>
  <span class="div" style="left:725px"></span>
  <a style="left:808px">Contact us</a>
  <span class="div" style="left:906px"></span>
  <span class="pointer"></span>
</nav>
<div class="abs search"><svg width="16" height="16" style="margin:5px 8px"><circle cx="6" cy="6" r="4.5" fill="none" stroke="#0a2d50" stroke-width="2"/><path d="M9.5 9.5l5 5" stroke="#0a2d50" stroke-width="2.5"/></svg></div>

<main class="abs main"></main>
<div class="abs vdiv"></div>
<div class="abs hdiv"></div>

<h2 style="left:58px;top:445px">WELCOME TO QVT</h2>
<p class="copy" style="left:58px;top:491px;width:552px">Lorem ipsum dolor sit amet, consectetuer adipiscing elit, sed diam nonummy nibh euismod tincidunt ut laoreet dolore magna aliquam erat volutpat. Ut wisi enim ad minim veniam, quis nostrud exerci tation ullamcorper suscipit lobortis nisl ut aliquip ex ea commodo consequat.</p>
<p class="copy" style="left:58px;top:579px;width:552px">Duis autem vel eum iriure dolor in hendrerit in vulputate velit esse molestie consequat, vel illum dolore eu feugiat nulla facilisis at vero eros et accumsan et iusto odio dignissim qui blandit praesent luptatum zzril delenit augue duis dolore te feugait nulla facilisi. Nam liber tempor cum soluta nobis eleifend option congue nihil imperdiet doming id quod mazim placerat facer possim assum.</p>
<div class="more" style="left:540px;top:671px"><span>&gt;&gt;</span> Read more</div>

<h2 style="left:58px;top:709px">Data Protection</h2>
<div class="ph" role="img" aria-label="Illustration of a cloud with a padlock" style="left:54px;top:746px;width:128px;height:156px;border-radius:40px 40px 10px 10px;background:linear-gradient(#8fd0f2,#3b8fc9 60%,#b59a55)"></div>
<p class="copy" style="left:200px;top:750px;width:410px">Lorem ipsum dolor sit amet, consectetuer adipiscing elit, sed diam nonummy nibh euismod tincidunt ut laoreet dolore magna aliquam erat volutpat. Ut wisi enim ad minim veniam, quis nostrud exerci tation ullamcorper suscipit lobortis nisl ut aliquip ex ea commodo consequat.</p>
<p class="copy" style="left:200px;top:855px;width:410px">Lorem ipsum dolor sit amet, consectetuer adipiscing elit, sed diam nonummy nibh euismod tincidunt ut laoreet dolore magna aliquam erat volutpat. Ut wisi enim ad minim veniam, quis</p>
<div class="more" style="left:540px;top:915px"><span>&gt;&gt;</span> Read more</div>

<h2 class="accent" style="left:674px;top:445px">Physical Security Services</h2>
<p class="copy" style="left:674px;top:488px;width:272px">Lorem ipsum dolor sit amet, consectetuer adipiscing elit, sed diam nonummy nibh euismod tincidunt ut laoreet dolore magna aliquam erat volutpat. Ut wisi enim ad minim veniam, quis nostrud exerci tation ullamcorper suscipit lobortis nisl ut aliquip ex ea commodo consequat.</p>
<div class="ph" role="img" aria-label="Photo of a security guard speaking into a radio outside an office building" style="left:962px;top:490px;width:184px;height:92px;background:linear-gradient(90deg,#4a79b0,#283a4e 55%,#6e7d88)"></div>
<p class="copy" style="left:674px;top:620px;width:480px">Duis autem vel eum iriure dolor in hendrerit in vulputate velit esse molestie consequat, vel illum dolore eu feugiat nulla facilisis at vero eros et accumsan et iusto odio dignissim qui blandit praesent luptatum zzril delenit augue duis dolore te feugait nulla facilisi. Nam liber tempor cum soluta nobis eleifend option congue nihil imperdiet doming id quod mazim .</p>
<div class="more" style="left:1061px;top:725px"><span>&gt;&gt;</span> Read more</div>

<h2 class="accent" style="left:680px;top:747px">Reach us</h2>
<address class="abs addr" style="font-style:normal">#12/21 Building name<br>Street Name<br>Avenue<br>Country - 345532<br><br>Tel: 1800 555 019<br>Email: info@qvt.example</address>
<div class="ph" role="img" aria-label="Street map showing the office location" style="left:920px;top:778px;width:238px;height:146px;border:3px solid #0a3560;background:linear-gradient(135deg,#e8e4da,#d9d4c6)"></div>

<footer class="abs footer">Copyright &copy; 2011 falkirkandassociates, <span style="display:inline-block;width:36px"></span><a href="#">Site Map</a> | <a href="#">Privacy Policy</a> | <a href="#">Terms &amp; Conditions</a> | <a href="#">Contact Us</a></footer>
<div class="abs social" aria-label="Social links">
  <i style="left:4px;background:#2f5aa0"></i>
  <i style="left:36px;background:#4aa3d8"></i>
  <i style="left:68px;background:#5b2a86"></i>
  <i style="left:100px;background:#2a7bb8"></i>
  <i style="left:132px;background:#e4602a"></i>
</div>
</body>
</html>
```